Kelvane Plumbing Business cards

Company is Kelvane Plumbing.
name Dashel Morrowby, I am a plumber, drainer, gasfitter and roofer
Mobile: 0431 906 154
Email address: info@kelvaneplumbing.example (check out my website for some ideas)
Website: www.kelvaneplumbing.example
ABN: 82 916 203 471
LIC: 604517K

I am reliable all round plumber. I am a 24 hour emergency service. Kelvane Plumbing is a professional plumbing service in the Illawarra, South Coast, Southern Sydney and Southern Highland regions of NSW. We offer a 24 hour emergency service for piece of mind to our customers. Call us now to see how we can help you. Kelvane Plumbing approaches every job with attention to detail and excellent customer service. With our superior workmanship you can be confident that the job will be done right the first time around. You can rest assured with results that are guaranteed to last.

Target Market(s)

the general public

Contact Information for Business Card

look up website for some ideas something with similar colours to logo and new modern and to catch the eye.

Colors
fdfdfd
ffffff
000000
7f7f7f
aaaaaa
33a6d7
0492cd

Requirements
Must have
• all contact details
• company- Kelvane Plumbing
• name- Dashel Morrowby
• number mobile- 0431 906 154
• Email address- info@kelvaneplumbing.example
• Website- www.kelvaneplumbing.example
• ABN- 82 916 203 471
• LIC- 604517K

```html
<!DOCTYPE html>
<html lang="en">
<head>
<meta charset="utf-8">
<title>Kelvane Plumbing – Business Cards</title>
<link rel="stylesheet" href="https://fonts.googleapis.com/css2?family=Montserrat:wght@300;400;500;700&display=swap">
<style>
  :root {
    --bg: #e9e9e9;
    --card: #0a0a0b;
    --white: #ffffff;
    --offwhite: #fdfdfd;
    --grey: #7f7f7f;
    --grey-light: #aaaaaa;
    --blue: #33a6d7;
    --blue-deep: #0492cd;
  }
  * { box-sizing: border-box; margin: 0; padding: 0; }
  html, body { width: 1200px; height: 831px; overflow: hidden; }
  body {
    background: var(--bg);
    font-family: "Montserrat", Arial, sans-serif;
    position: relative;
  }
  .card {
    position: absolute;
    width: 540px;
    height: 309px;
    background: var(--card);
    border-radius: 4px;
    box-shadow: 0 10px 30px rgba(0,0,0,.25);
    overflow: hidden;
  }
  .card--front { left: 50px; top: 110px; }
  .card--back  { left: 610px; top: 410px; }

  .brand {
    position: absolute;
    display: flex;
    align-items: center;
    gap: 10px;
    color: var(--blue);
    font-weight: 700;
    text-transform: uppercase;
    letter-spacing: .04em;
    white-space: nowrap;
  }
  .brand__dot {
    border-radius: 50%;
    background: var(--blue);
    flex: none;
  }
  .card--front .brand { left: 50%; top: 50%; transform: translate(-50%,-50%); font-size: 28px; }
  .card--front .brand__dot { width: 22px; height: 22px; }
  .card--back .brand { left: 300px; top: 62px; font-size: 18px; }
  .card--back .brand__dot { width: 14px; height: 14px; }

  .rule {
    position: absolute;
    left: 40px; right: 40px; top: 150px;
    height: 1px;
    background: var(--offwhite);
  }
  .rule::before, .rule::after {
    content: "";
    position: absolute;
    top: -6px;
    width: 1px; height: 13px;
    background: var(--offwhite);
  }
  .rule::before { left: 0; }
  .rule::after { right: 0; }

  .person {
    position: absolute;
    right: 48px; top: 116px;
    font-size: 26px;
    letter-spacing: .02em;
    text-transform: uppercase;
  }
  .person__first { color: var(--grey-light); font-weight: 300; }
  .person__last { color: var(--blue); font-weight: 700; }

  .contacts {
    position: absolute;
    left: 40px; top: 172px;
    list-style: none;
  }
  .contacts li {
    display: flex;
    align-items: center;
    gap: 10px;
    color: var(--white);
    font-size: 14.5px;
    margin-bottom: 11px;
  }
  .contacts .icon {
    width: 16px; height: 16px;
    border-radius: 50%;
    background: var(--blue);
    display: flex; align-items: center; justify-content: center;
    flex: none;
  }
  .contacts svg { width: 10px; height: 10px; }

  .credentials {
    position: absolute;
    right: 40px; top: 220px;
    text-align: right;
    color: var(--white);
    font-size: 15px;
    line-height: 1.9;
    letter-spacing: .02em;
  }
</style>
</head>
<body>

<section class="card card--front" aria-label="Card front">
  <div class="brand"><span class="brand__dot"></span>Kelvane Plumbing</div>
</section>

<section class="card card--back" aria-label="Card back">
  <div class="brand"><span class="brand__dot"></span>Kelvane Plumbing</div>

  <h1 class="person"><span class="person__first">Dashel</span> <span class="person__last">Morrowby</span></h1>
  <div class="rule"></div>

  <ul class="contacts">
    <li>
      <span class="icon"><svg viewBox="0 0 10 10"><path d="M2.2 1l1.5 1.7-.8 1a5 5 0 0 0 2.4 2.4l1-.8L8 6.8 7.3 8.6C4.2 8.4 1.6 5.8 1.4 2.7z" fill="#0a0a0b"/></svg></span>
      0431 906 154
    </li>
    <li>
      <span class="icon"><svg viewBox="0 0 10 10"><rect x="1" y="2.3" width="8" height="5.4" fill="#0a0a0b"/><path d="M1.3 2.6L5 5.4l3.7-2.8" stroke="#33a6d7" stroke-width=".8" fill="none"/></svg></span>
      info@kelvaneplumbing.example
    </li>
    <li>
      <span class="icon"><svg viewBox="0 0 10 10" fill="none" stroke="#0a0a0b" stroke-width=".9"><circle cx="5" cy="5" r="3.8"/><ellipse cx="5" cy="5" rx="1.6" ry="3.8"/><path d="M1.2 5h7.6"/></svg></span>
      www.kelvaneplumbing.example
    </li>
  </ul>

  <div class="credentials">
    <p>ABN- 82 916 203 471</p>
    <p>LIC- 604517K</p>
  </div>
</section>

</body>
</html>
```